KB Rubbish Removal Business Card

Hey,
I need a double sided business card designed for a rubbish removal business based in Australia. Logo is already chosen, similar colours preferred for both sides of the business card.

Details to include:

Front:

KB Rubbish Removal
Darren Holloway
Managing Director
Mobile: 0471 902 146
Email: darren@kbrubbishremoval.com.au
Website: kbrubbishremoval.com.au

Rear:

How did we do?
kbrubbishremoval.com.au/review

```html
<!DOCTYPE html>
<html lang="en">
<head>
<meta charset="utf-8">
<title>KB Rubbish Removal Business Card</title>
<link rel="stylesheet" href="https://fonts.googleapis.com/css2?family=Roboto:wght@300;400;500;700&display=swap">
<style>
  :root {
    --backdrop: #58585a;
    --card: #ffffff;
    --ink: #58595b;
    --forest: #146f36;
    --leaf: #2bab4b;
    --grass: #3bb54a;
  }
  html, body {
    margin: 0;
    padding: 0;
    width: 1200px;
    height: 1200px;
    overflow: hidden;
    background: var(--backdrop);
  }
  .stage {
    position: absolute;
    left: 0;
    top: 0;
    width: 1772px;
    height: 1772px;
    transform: scale(0.67720);
    transform-origin: 0 0;
    font-family: "Roboto", Arial, sans-serif;
    color: var(--ink);
  }
  .card {
    position: absolute;
    left: 342px;
    width: 1087px;
    height: 634px;
    background: var(--card);
    overflow: hidden;
  }
  .card--front { top: 274px; }
  .card--back { top: 984px; }
  .card__accent {
    position: absolute;
    inset: 0;
    width: 100%;
    height: 100%;
  }
  .text { position: absolute; margin: 0; line-height: 1; white-space: nowrap; }
  .person__name { left: 247px; top: 222px; font-size: 38px; font-weight: 700; letter-spacing: -0.3px; }
  .person__role { left: 247px; top: 266px; font-size: 28px; font-weight: 300; }
  .contact { left: 246px; font-size: 28px; font-weight: 300; display: flex; align-items: center; }
  .contact svg { width: 22px; height: 22px; margin-right: 10px; fill: var(--ink); }
  .contact--phone { top: 350px; }
  .contact--web { top: 410px; }
  .contact--mail { top: 469px; }
  .brand { left: 232px; top: 233px; font-size: 38px; font-weight: 700; letter-spacing: -0.3px; }
  .review__title { left: 230px; top: 283px; font-size: 75px; font-weight: 700; letter-spacing: -1px; }
  .review__link { left: 232px; top: 360px; font-size: 28px; font-weight: 300; }
</style>
</head>
<body>
<div class="stage">

  <section class="card card--front">
    <svg class="card__accent" viewBox="0 0 1087 634" role="img" aria-label="Green decorative accent areas along the top right and lower left corner">
      <defs>
        <linearGradient id="frontTone" x1="0" y1="0" x2="1" y2="1">
          <stop offset="0" stop-color="var(--grass)"/>
          <stop offset="1" stop-color="var(--forest)"/>
        </linearGradient>
        <linearGradient id="frontCornerTone" x1="0" y1="0" x2="1" y2="1">
          <stop offset="0" stop-color="var(--leaf)"/>
          <stop offset="1" stop-color="var(--forest)"/>
        </linearGradient>
      </defs>
      <path fill="url(#frontTone)" d="M0,0 H1087 V430 C930,430 820,340 760,230 C700,130 600,100 460,110 C300,120 140,120 0,70 Z"/>
      <path fill="url(#frontCornerTone)" d="M0,410 A230,224 0 0 1 230,634 L0,634 Z"/>
    </svg>

    <h1 class="text person__name">Darren Holloway</h1>
    <p class="text person__role">Managing Director</p>

    <p class="text contact contact--phone">
      <svg viewBox="0 0 22 22" aria-hidden="true"><path d="M5,0 H17 A2,2 0 0 1 19,2 V20 A2,2 0 0 1 17,22 H5 A2,2 0 0 1 3,20 V2 A2,2 0 0 1 5,0 Z M5.5,3 V16 H16.5 V3 Z M11,17.3 A1.5,1.5 0 1 0 11,20.3 A1.5,1.5 0 1 0 11,17.3 Z"/></svg>
      0471 902 146
    </p>
    <p class="text contact contact--web">
      <svg viewBox="0 0 22 22" aria-hidden="true"><path fill-rule="evenodd" d="M11,1 A10,10 0 1 0 11,21 A10,10 0 1 0 11,1 Z M11,3 C9.5,5 8.8,7.5 8.7,10 H13.3 C13.2,7.5 12.5,5 11,3 Z M3.1,10 H6.7 C6.8,7.8 7.3,5.5 8.3,3.6 A8,8 0 0 0 3.1,10 Z M15.3,10 H18.9 A8,8 0 0 0 13.7,3.6 C14.7,5.5 15.2,7.8 15.3,10 Z M3.1,12 A8,8 0 0 0 8.3,18.4 C7.3,16.5 6.8,14.2 6.7,12 Z M8.7,12 C8.8,14.5 9.5,17 11,19 C12.5,17 13.2,14.5 13.3,12 Z M15.3,12 C15.2,14.2 14.7,16.5 13.7,18.4 A8,8 0 0 0 18.9,12 Z"/></svg>
      kbrubbishremoval.com.au
    </p>
    <p class="text contact contact--mail">
      <svg viewBox="0 0 22 22" aria-hidden="true"><path d="M1,5 H21 V17 H1 Z M2.5,6.3 V15.7 L7.5,11 Z M19.5,6.3 L14.5,11 L19.5,15.7 Z M3.3,6 L11,12.5 L18.7,6 Z M8.6,12 L3.3,16 H18.7 L13.4,12 L11,14 Z" fill-rule="evenodd"/></svg>
      darren@kbrubbishremoval.com.au
    </p>
  </section>

  <section class="card card--back">
    <svg class="card__accent" viewBox="0 0 1087 634" role="img" aria-label="Green decorative accent areas in the top right and lower left">
      <defs>
        <linearGradient id="backTone" x1="0" y1="0" x2="1" y2="1">
          <stop offset="0" stop-color="var(--forest)"/>
          <stop offset="1" stop-color="var(--leaf)"/>
        </linearGradient>
        <linearGradient id="backCornerTone" x1="0" y1="0" x2="1" y2="1">
          <stop offset="0" stop-color="var(--leaf)"/>
          <stop offset="1" stop-color="var(--forest)"/>
        </linearGradient>
      </defs>
      <path fill="url(#backTone)" d="M660,0 H1087 V390 C880,390 770,260 730,130 C712,70 690,30 660,0 Z"/>
      <path fill="url(#backCornerTone)" d="M0,170 C120,250 140,560 520,580 C640,585 740,600 810,634 L0,634 Z"/>
    </svg>

    <h2 class="text brand">KB Rubbish Removal</h2>
    <p class="text review__title">How did we do?</p>
    <p class="text review__link">kbrubbishremoval.com.au/review</p>
  </section>

</div>
</body>
</html>
```